Medigap Insurance Interactive website

We are looking at redesigning our website for a more up to date and responsive look and feel. We will code this site using Bootstrap 3 so please research and know how to design for this. Attached is our logo and a wireframe for the new site.
I look forward to seeing what you guys can do.

Target Market(s)

People elegible for Medigap Insurance in the US

Industry/Entity Type

Insurance

Number of Pages Required

5+ page

Font styles to use
Sans Serif

Requirements
Must have
• Match the logo
• Be Bootstrap 3 compatible design
• Font Awesome Icons

```html
<!DOCTYPE html>
<html lang="en">
<head>
<meta charset="utf-8">
<title>Careway – Medicare Supplement Plans</title>
<link href="https://fonts.googleapis.com/css2?family=Bree+Serif&family=Lato:ital,wght@0,400;0,700;1,400&display=swap" rel="stylesheet">
<style>
:root{
  --navy:#0b2f66;
  --navy-dark:#062656;
  --red:#c8201e;
  --ink:#1a1a1a;
  --page:#f4f4f4;
  --band:#f8f8f8;
  --line:#dcdcdc;
}
*{box-sizing:border-box;margin:0;padding:0}
html,body{width:1200px;height:1018px;overflow:hidden}
body{background:var(--page);font-family:'Lato',sans-serif;color:var(--ink);position:relative}

/* top bar */
.topbar{position:absolute;top:0;left:0;width:1200px;height:35px;background:var(--navy-dark)}
.topbar .phone{position:absolute;left:80px;top:7px;display:flex;align-items:center;gap:7px;color:#fff;font-weight:700;font-size:16px}
.topbar .phone .ico{width:21px;height:21px;border-radius:50%;background:var(--red);display:flex;align-items:center;justify-content:center}
.social{position:absolute;right:80px;top:7px;display:flex;gap:6px}
.social span{width:21px;height:21px;border-radius:50%;background:var(--red)}

/* header */
.header{position:absolute;top:35px;left:0;width:1200px;height:90px;background:#fafafa}
.brand{position:absolute;left:82px;top:24px;font-family:'Lato',sans-serif;font-weight:700;font-size:36px;color:var(--navy);line-height:1;letter-spacing:1px}
.nav{position:absolute;right:80px;top:38px;display:flex;font-family:'Bree Serif',serif;font-size:15px}
.nav a{color:#111;text-decoration:none;padding:0 13px;border-left:1px solid #999;line-height:13px;height:14px;display:block}
.nav a:first-child{border-left:0;color:var(--red);position:relative;padding-left:0}
.nav a:first-child::after{content:"";position:absolute;left:0;right:13px;top:23px;height:3px;background:var(--navy)}
.nav a:last-child{padding-right:0}

/* hero */
.hero{position:absolute;top:125px;left:0;width:1200px;height:441px;background:linear-gradient(100deg,#6b5a4f 0%,#8d7f75 30%,#9aa3aa 60%,#7d8a94 100%)}
.video{position:absolute;left:745px;top:47px;width:373px;height:304px;border:1px solid var(--navy);background:linear-gradient(135deg,#c9ccd0,#8f959c 60%,#6f7780)}
.video .play-big{position:absolute;left:152px;top:112px;width:70px;height:48px;border-radius:9px;background:rgba(60,60,60,.75)}
.video .controls{position:absolute;left:0;bottom:0;width:100%;height:33px;background:#111;color:#fff;font-size:13px;display:flex;align-items:center;padding:0 10px;gap:10px}
.controls .bar{flex:1;height:9px;border-radius:5px;background:#3a3a3a;position:relative}
.controls .bar::before{content:"";position:absolute;left:0;top:0;width:62%;height:100%;border-radius:5px;background:#555}
.controls .bar::after{content:"";position:absolute;left:60%;top:-1px;width:11px;height:11px;border-radius:50%;background:#888}
.caption{position:absolute;left:0;top:371px;width:100%;height:70px;background:rgba(120,120,120,.55)}
.caption h1{position:absolute;left:132px;top:17px;font-family:'Bree Serif',serif;font-weight:400;font-size:31px;color:#fff;text-shadow:0 1px 2px rgba(0,0,0,.3)}
.btn-quote{position:absolute;left:937px;top:15px;width:130px;height:40px;background:var(--red);color:#fff;font-size:17px;display:flex;align-items:center;justify-content:center;border-radius:2px}

/* features */
.features{position:absolute;top:566px;left:0;width:1200px;height:127px;background:var(--band);border:1px solid var(--line)}
.feature{position:absolute;top:33px;display:flex;gap:8px}
.feature .circle{width:60px;height:60px;border-radius:50%;background:var(--navy);display:flex;align-items:center;justify-content:center}
.feature h3{font-family:'Bree Serif',serif;font-weight:400;color:var(--navy);font-size:18px;margin-top:2px}
.btn-more{display:inline-block;margin-top:6px;background:var(--red);color:#fff;font-size:12px;font-weight:700;padding:3px 11px}
.chev{position:absolute;top:14px}

/* content */
.col{position:absolute;top:728px}
.col h2{font-family:'Bree Serif',serif;font-weight:400;font-size:20px;color:var(--navy);display:inline-block;position:relative;padding-bottom:3px}
.col h2 .r{color:var(--red);position:relative}
.col h2::after{content:"";position:absolute;left:0;bottom:-2px;width:58%;height:2px;background:var(--navy)}
.col h2 .r::after{content:"";position:absolute;left:0;right:0;bottom:-5px;height:2px;background:var(--red)}
.about h2::after{width:55%}
.about p{margin-top:14px;margin-left:4px;width:320px;font-size:14px;line-height:18.5px;color:#222}
.divider{position:absolute;top:740px;width:1px;height:200px;background:#e2e2e2}
.quote{margin-top:14px;width:292px;background:#fff;border-radius:8px;padding:12px 16px;font-style:italic;font-size:13px;line-height:20px;color:#555;position:relative;box-shadow:0 1px 3px rgba(0,0,0,.06)}
.quote::after{content:"";position:absolute;left:158px;bottom:-12px;border-left:14px solid #fff;border-bottom:12px solid transparent}
.author{display:flex;align-items:center;gap:18px;margin-top:2px;margin-left:15px}
.author .avatar{width:76px;height:76px;border-radius:50%;border:4px solid #fff;background:linear-gradient(135deg,#c08a68,#6e8fa8);box-shadow:0 1px 4px rgba(0,0,0,.25)}
.author span{font-weight:700;font-size:14px;color:#333;margin-top:-12px}
.updates p{margin-top:14px;font-size:14.5px;line-height:19px;width:320px}
.field{margin-top:15px;width:322px;height:35px;border:1px solid #ccc;border-radius:3px;background:#f0f0f0;color:#777;font-size:14px;padding:8px 9px}
.btn-sign{margin-top:16px;width:74px;height:31px;background:var(--navy);color:#fff;font-size:14px;border-radius:2px;display:flex;align-items:center;justify-content:center}

/* footer */
.footer{position:absolute;top:972px;left:0;width:1200px;height:46px;background:var(--navy-dark);color:#fff;font-size:14px}
.footer .copy{position:absolute;left:79px;top:15px}
.footer .links{position:absolute;right:80px;top:15px}
.footer .links span{margin:0 5px}
</style>
</head>
<body>

<div class="topbar">
  <div class="phone">
    <span class="ico"><svg width="11" height="11" viewBox="0 0 24 24"><path fill="#fff" d="M6.6 10.8a15 15 0 0 0 6.6 6.6l2.2-2.2c.3-.3.7-.4 1-.2 1.1.4 2.3.6 3.6.6.6 0 1 .4 1 1V20c0 .6-.4 1-1 1A17 17 0 0 1 3 4c0-.6.4-1 1-1h3.5c.6 0 1 .4 1 1 0 1.3.2 2.5.6 3.6.1.3 0 .7-.2 1z"/></svg></span>
    (800) 555-0142
  </div>
  <div class="social" aria-label="Social links"><span></span><span></span><span></span><span></span></div>
</div>

<header class="header">
  <div class="brand">CAREWAY</div>
  <nav class="nav">
    <a href="#">Medicare Supplement</a>
    <a href="#">Part D</a>
    <a href="#">How To Decide</a>
    <a href="#">Learn Online</a>
    <a href="#">Why Careway</a>
    <a href="#">Buy Now</a>
  </nav>
</header>

<section class="hero" role="img" aria-label="Smiling family of three by the seaside">
  <div class="video" role="img" aria-label="Video thumbnail of advisors reviewing papers with a client">
    <div class="play-big"><svg width="70" height="48"><path d="M31 16l14 8-14 8z" fill="#fff"/></svg></div>
    <div class="controls">
      <svg width="14" height="14"><path d="M2 1l11 6-11 6z" fill="#fff"/></svg>
      <span>04:59</span>
      <div class="bar"></div>
      <span>10:35</span>
      <svg width="18" height="16" viewBox="0 0 18 16"><path d="M1 5h4l5-4v14l-5-4H1z" fill="#fff"/><path d="M13 4q3 4 0 8" stroke="#fff" fill="none" stroke-width="1.6"/></svg>
      <svg width="18" height="18" viewBox="0 0 18 18"><path d="M2 2h6L2 8zM16 16h-6l6-6zM4 4l10 10" stroke="#fff" fill="#fff" stroke-width="1.5"/></svg>
    </div>
  </div>
  <div class="caption">
    <h1>It's Time To Take Action And Protect What Matters Most</h1>
    <div class="btn-quote">GET QUOTE</div>
  </div>
</section>

<section class="features">
  <div class="feature" style="left:80px">
    <div class="circle"><svg width="30" height="30" viewBox="0 0 30 30" fill="none" stroke="#fff" stroke-width="3"><path d="M9 25V8M5 12l4-5 4 5M21 5v17M17 18l4 5 4-5"/></svg></div>
    <div><h3>Compare Rates</h3><span class="btn-more">Read More</span></div>
  </div>
  <svg class="chev" style="left:306px" width="46" height="100"><path d="M4 0l40 50-40 50" stroke="#fff" stroke-width="8" fill="none"/></svg>
  <div class="feature" style="left:385px">
    <div class="circle"><svg width="32" height="32" viewBox="0 0 32 32"><text x="16" y="15" text-anchor="middle" font-size="15" font-family="Lato" font-weight="700" fill="#fff">$</text><path d="M4 22h8l6 2h7c2 0 3-2 1-3l-8-2" stroke="#fff" stroke-width="2.2" fill="none"/></svg></div>
    <div><h3>Buy Now</h3><span class="btn-more">Read More</span></div>
  </div>
  <svg class="chev" style="left:567px" width="46" height="100"><path d="M4 0l40 50-40 50" stroke="#fff" stroke-width="8" fill="none"/></svg>
  <div class="feature" style="left:648px">
    <div class="circle"><svg width="32" height="26" viewBox="0 0 32 26"><rect x="5" y="2" width="22" height="15" rx="1" fill="#fff"/><path d="M2 20h28l-2 3H4z" fill="#fff"/><ellipse cx="16" cy="9.5" rx="6" ry="3.5" fill="#0b2f66"/><circle cx="16" cy="9.5" r="1.8" fill="#fff"/></svg></div>
    <div><h3>Learn Online</h3><span class="btn-more">Read More</span></div>
  </div>
  <svg class="chev" style="left:850px" width="46" height="100"><path d="M4 0l40 50-40 50" stroke="#fff" stroke-width="8" fill="none"/></svg>
  <div class="feature" style="left:930px">
    <div class="circle"><svg width="34" height="34" viewBox="0 0 34 34" fill="none" stroke="#fff" stroke-width="2.4"><path d="M6 19v-4a11 11 0 0 1 22 0v4"/><rect x="3" y="17" width="5" height="8" rx="2" fill="#fff"/><rect x="26" y="17" width="5" height="8" rx="2" fill="#fff"/><circle cx="17" cy="19" r="7"/><path d="M26 25q-2 5-8 5"/></svg></div>
    <div><h3>Get Expert Help</h3><span class="btn-more">Read More</span></div>
  </div>
</section>

<section class="col about" style="left:79px">
  <h2>About <span class="r">CAREWAY</span> Plans</h2>
  <p>Lorem ipsum dolor sit amet, consectetur adipiscing elit. Sed vitae magna tellus. Aenean ante nunc, semper nec cursus non, rutrum ac eros. Vestibulum mattis justo ac dui bibendum consequat a ac ipsum. Praesent a arcu venenatis, auctor velit eu, suscipit libero. Quisque convallis, leo ac pharetra sagittis, ipsum arcu auctor urna, sit amet cursus risus augue in eros sit amet cursus.</p>
</section>
<div class="divider" style="left:427px"></div>

<section class="col testimonial" style="left:454px">
  <h2>What People <span class="r">Are Saying</span></h2>
  <div class="quote">“ Lorem ipsum dolor sit amet conetuge sed diay nibhdl tincidunt ut laoreet dolore magam er vol wisi enim ad minim vni quis nostrud exerci tationorem ipsum...</div>
  <div class="author">
    <div class="avatar" role="img" aria-label="Portrait of the customer"></div>
    <span>Mr.Owen Hartley</span>
  </div>
</section>
<div class="divider" style="left:770px"></div>

<section class="col updates" style="left:798px">
  <h2>Monthly <span class="r">Updates</span></h2>
  <p>Enter Your Email for Customized Monthly Rate Update and More..</p>
  <div class="field">Enter Email Id</div>
  <div class="btn-sign">Sign In</div>
</section>

<footer class="footer">
  <div class="copy">Copyright © 2016 CAREWAY. All Rights Reserved.</div>
  <div class="links">Sitemap<span>|</span>Buy Now<span>|</span>Blog<span>|</span>Login</div>
</footer>

</body>
</html>
```